2019 2020 School Leavers Flyer

refer attached hoodie and tee shirts flyers for 2018, we just require an updated version showing 2019 and 2020 designs.we would like to do it as an A3 flyer folded to A4, so we will need a front and back cover.we would also like to use our new QBR logo (different versions attached) happy for any to be used creatively.back cover could be an advertisement that gets customers to visit our website.www.gallowayteamstore.com.au
Target Market(s)
Schools buying leavers tee shirts and hoodies for their students
Font styles to use
Requirements
Must have
- plenty of design options similar to flyers i have already attached
Nice to have
- back page , just an advertisement to get visitors to our website

```html
<!DOCTYPE html>
<html lang="en">
<head>
<meta charset="utf-8">
<title>QBR 2019-20 School Leavers Flyer</title>
<link rel="stylesheet" href="https://fonts.googleapis.com/css2?family=Oswald:wght@500;600;700&family=Open+Sans:wght@400;600;700&display=swap">
<style>
  :root {
    --bg: #c9c8c8;
    --paper: #ffffff;
    --ink: #151515;
    --red: #e11b22;
    --navy: #1c2b45;
    --steel: #3c5675;
    --amber: #8a6a3c;
    --blue: #1f4fa8;
    --garment-dark: #24283a;
    --garment-pink: #b8426e;
    --yellow: #f3d21c;
    --grey-text: #2d3a55;
  }
  * { box-sizing: border-box; margin: 0; padding: 0; }
  html, body { width: 913px; height: 1200px; overflow: hidden; }
  body { background: var(--bg); font-family: "Open Sans", Arial, sans-serif; position: relative; }

  .spread {
    position: absolute; left: 36px; top: 303px;
    width: 840px; height: 594px; display: flex;
    box-shadow: 0 10px 30px rgba(0,0,0,.25);
  }
  .page { position: relative; width: 420px; height: 594px; background: var(--paper); overflow: hidden; }

  /* Back cover */
  .back-frame { position: absolute; inset: 26px; border: 2px solid var(--red); }
  .garments {
    position: absolute; left: 78px; top: 66px; width: 264px; height: 196px;
    border-radius: 8px;
    background: linear-gradient(125deg, var(--blue) 0%, #2b4f96 30%, var(--garment-dark) 60%, var(--garment-pink) 100%);
  }
  .checklist {
    position: absolute; left: 60px; top: 290px; width: 300px;
    display: grid; grid-template-columns: repeat(3, auto); gap: 6px 14px; justify-content: center;
    font-size: 10px; color: var(--grey-text);
  }
  .checklist li { list-style: none; display: flex; align-items: center; gap: 4px; white-space: nowrap; }
  .tick { width: 9px; height: 9px; flex: none; }
  .web-ad {
    position: absolute; left: 56px; top: 345px; width: 308px; height: 100px;
    background: var(--blue); border: 3px solid #ffffff; outline: 1px solid var(--blue);
    color: #fff; text-align: center; padding-top: 16px;
  }
  .web-ad .lead { color: var(--yellow); font-size: 12px; }
  .web-ad .sub { font-size: 12px; margin-top: 2px; }
  .web-ad .url { font-size: 18px; margin-top: 6px; white-space: nowrap; }
  .web-ad .url b { color: var(--yellow); font-weight: 700; }
  .social { position: absolute; left: 0; right: 0; top: 470px; display: flex; justify-content: center; gap: 10px; }
  .social span { width: 16px; height: 16px; border-radius: 50%; background: var(--blue); }
  .social span:nth-child(2) { background: #c0406a; }
  .social span:nth-child(3) { background: #2a9fe0; }
  .social span:nth-child(4) { background: var(--red); }

  /* Front cover */
  .brand { position: absolute; top: 22px; left: 0; right: 0; display: flex; justify-content: center; align-items: center; gap: 8px; }
  .brand-dot { width: 14px; height: 14px; border-radius: 50%; background: var(--red); }
  .brand-name { font-family: "Oswald", sans-serif; font-weight: 700; font-size: 34px; line-height: 1; color: var(--ink); letter-spacing: 1px; }
  .brand-tag { font-family: "Oswald", sans-serif; font-weight: 700; font-size: 9px; color: var(--ink); letter-spacing: 1px; }
  .hero {
    position: absolute; left: 0; right: 0; top: 92px; height: 384px;
    background: linear-gradient(160deg, var(--amber) 0%, var(--steel) 30%, var(--navy) 65%, #2f4561 100%);
  }
  .hero-frame { position: absolute; left: 0; top: 0; }
  .title { position: absolute; left: 44px; top: 96px; font-family: "Oswald", sans-serif; font-weight: 600; line-height: .95; }
  .title .years { color: var(--red); font-size: 56px; }
  .title .words { color: #fff; font-size: 60px; }
  .url-band {
    position: absolute; left: 70px; right: 70px; top: 508px; height: 22px;
    background: var(--red); color: #fff; font-size: 11px; font-weight: 600;
    display: flex; align-items: center; justify-content: center;
  }
</style>
</head>
<body>
<main class="spread">
  <section class="page back-cover">
    <div class="back-frame"></div>
    <div class="garments" role="img" aria-label="Assorted team garments — polo, singlets, jacket and netball dress — over a blue paint brush stroke"></div>
    <ul class="checklist">
      <li><svg class="tick" viewBox="0 0 10 10"><rect x=".5" y=".5" width="9" height="9" fill="none" stroke="#2d3a55"/><path d="M2 5l2 2 4-4" fill="none" stroke="#2d3a55" stroke-width="1.2"/></svg>Polo Shirt</li>
      <li><svg class="tick" viewBox="0 0 10 10"><rect x=".5" y=".5" width="9" height="9" fill="none" stroke="#2d3a55"/><path d="M2 5l2 2 4-4" fill="none" stroke="#2d3a55" stroke-width="1.2"/></svg>Tee Shirt</li>
      <li><svg class="tick" viewBox="0 0 10 10"><rect x=".5" y=".5" width="9" height="9" fill="none" stroke="#2d3a55"/><path d="M2 5l2 2 4-4" fill="none" stroke="#2d3a55" stroke-width="1.2"/></svg>Team Singlet</li>
      <li><svg class="tick" viewBox="0 0 10 10"><rect x=".5" y=".5" width="9" height="9" fill="none" stroke="#2d3a55"/><path d="M2 5l2 2 4-4" fill="none" stroke="#2d3a55" stroke-width="1.2"/></svg>Basketball Singlet</li>
      <li><svg class="tick" viewBox="0 0 10 10"><rect x=".5" y=".5" width="9" height="9" fill="none" stroke="#2d3a55"/><path d="M2 5l2 2 4-4" fill="none" stroke="#2d3a55" stroke-width="1.2"/></svg>Track Jacket</li>
      <li><svg class="tick" viewBox="0 0 10 10"><rect x=".5" y=".5" width="9" height="9" fill="none" stroke="#2d3a55"/><path d="M2 5l2 2 4-4" fill="none" stroke="#2d3a55" stroke-width="1.2"/></svg>Netball Dress, etc..</li>
    </ul>
    <div class="web-ad">
      <p class="lead">Vew more Design of hoodie and tee shirts</p>
      <p class="sub">at our website</p>
      <p class="url">www.<b>gallowayteamstore</b>.com.au</p>
    </div>
    <div class="social" aria-label="Social channels"><span></span><span></span><span></span><span></span></div>
  </section>

  <section class="page front-cover">
    <div class="brand">
      <span class="brand-dot"></span>
      <div class="brand-text">
        <div class="brand-name">QBR</div>
        <div class="brand-tag">GALLOWAY TEAM STORE</div>
      </div>
    </div>
    <div class="hero" role="img" aria-label="Young athlete in a zip hoodie and shorts running through a concrete underpass">
      <svg class="hero-frame" width="420" height="384" viewBox="0 0 420 384">
        <g fill="none" stroke="#ffffff" stroke-width="3">
          <polyline points="38,92 38,50 230,50"/>
          <polyline points="290,50 370,50 370,200"/>
          <polyline points="370,250 370,330 230,330"/>
          <polyline points="60,330 38,330 38,270"/>
        </g>
      </svg>
      <h1 class="title">
        <span class="years">2019-20</span><br>
        <span class="words">SCHOOL<br>LEAVERS</span>
      </h1>
    </div>
    <div class="url-band">www.gallowayteamstore.com.au</div>
  </section>
</main>
</body>
</html>
```